BQL Groundworks & Freight Business Card

Can you please design a business card for an Earthworks, Haulage truck and machinery hire company. They also provide sand soil and mulch supply, as well as screening of products. Can you re-create the logo from the attached but add BQL Groundworks & Freight just use the three diamond design.

Target Market(s)

Earthmoving and Transport, Landscapers, Construction

Contact Information for Business Card

ABN 52 907 334 816, Doug Pelham, Managing Director, BQL Groundworks & Freight Mobile 0438 256 904 Email bqlfreight2010@mailvane.net

Font styles to use
Sans Serif

Colors
ec1f27
000000
cbcbcb
ffffff

Requirements
Must have
• Listed on the back, Earthworks | Haulage | Truck and Machinery Hire | Sand, Soil & Mulch Supply | Screening of Products
Nice to have
• Would be good for it to look appealing to a mans man, because it relates to heavy machinery, earthworks, construction etc. Black, red and white would be good maybe with a bit of silver somewhere.
Should not have
• not sure

```html
<!DOCTYPE html>
<html lang="en">
<head>
<meta charset="utf-8">
<title>BQL Groundworks &amp; Freight Business Card</title>
<link href="https://fonts.googleapis.com/css2?family=Exo+2:wght@400;600;700&display=swap" rel="stylesheet">
<style>
  :root {
    --bg: #2f3e45;
    --card: #262626;
    --card-edge: #1c1c1c;
    --corner: #555555;
    --red: #ec1f27;
    --brand-red: #b3161d;
    --white: #ffffff;
    --silver: #cbcbcb;
    --muted: #a9a9a9;
  }
  * { box-sizing: border-box; margin: 0; padding: 0; }
  html, body { width: 1200px; height: 900px; overflow: hidden; }
  body {
    background: var(--bg);
    font-family: "Exo 2", Arial, sans-serif;
    color: var(--white);
    position: relative;
  }
  .card {
    position: absolute;
    left: 250px;
    width: 700px;
    height: 400px;
    background: linear-gradient(135deg, #2b2b2b, var(--card-edge));
    overflow: hidden;
    box-shadow: 0 10px 30px rgba(0,0,0,.4);
  }
  .card--details { top: 30px; }
  .card--brand { top: 470px; }
  .card__corners { position: absolute; inset: 0; width: 700px; height: 400px; }

  /* Details side */
  .details__brand {
    position: absolute; left: 40px; top: 55px; width: 330px;
    text-align: center;
  }
  .tagline { font-size: 19px; letter-spacing: 1.5px; line-height: 1.35; color: var(--white); }
  .wordmark {
    display: flex; align-items: center; justify-content: center; gap: 14px;
    margin: 22px 0 14px;
  }
  .wordmark__square { width: 22px; height: 22px; background: var(--brand-red); }
  .wordmark__name { font-weight: 700; color: var(--brand-red); letter-spacing: 6px; line-height: 1; }
  .details__brand .wordmark__name { font-size: 58px; }
  .company { font-weight: 700; line-height: 1.1; color: var(--white); }
  .details__brand .company { font-size: 24px; letter-spacing: 1px; }

  .divider-v {
    position: absolute; left: 385px; top: 35px; width: 2px; height: 215px;
    background: linear-gradient(to bottom, transparent, var(--silver), transparent);
  }
  .contact {
    position: absolute; left: 400px; top: 70px; width: 290px; text-align: center;
  }
  .contact__name { font-size: 27px; font-weight: 700; color: var(--silver); letter-spacing: 1px; line-height: 1; }
  .contact__role { font-size: 15px; letter-spacing: 2.5px; margin-top: 2px; }
  .contact__phone { font-size: 25px; font-weight: 700; letter-spacing: 2px; margin-top: 8px; }
  .contact__abn { font-size: 18px; color: var(--muted); letter-spacing: 1.5px; line-height: 1.3; margin-top: 14px; }

  /* Brand side */
  .brand {
    position: absolute; left: 0; right: 0; top: 34px; text-align: center;
  }
  .brand .wordmark { margin: 0 0 12px; }
  .brand .wordmark__square { width: 30px; height: 30px; }
  .brand .wordmark__name { font-size: 80px; }
  .brand .company { font-size: 34px; letter-spacing: 1px; }
  .services {
    position: absolute; left: 90px; right: 90px; top: 228px;
    text-align: center; font-size: 13px; line-height: 18px;
    letter-spacing: 1px; color: var(--silver);
  }
  .divider-h {
    position: absolute; left: 150px; right: 130px; top: 276px; height: 2px;
    background: linear-gradient(to right, transparent, var(--silver), transparent);
  }
  .brand__contact { position: absolute; left: 0; right: 0; top: 292px; text-align: center; }
  .brand__phone { font-size: 34px; font-weight: 700; color: var(--silver); letter-spacing: 2px; line-height: 1.2; }
  .brand__email { font-size: 23px; letter-spacing: 4px; color: var(--silver); margin-top: 2px; }
</style>
</head>
<body>

<section class="card card--details" aria-label="Business card, contact side">
  <svg class="card__corners" viewBox="0 0 700 400" aria-hidden="true">
    <polygon points="0,0 270,0 0,80" fill="var(--corner)"/>
    <line x1="0" y1="80" x2="270" y2="0" stroke="var(--red)" stroke-width="6"/>
    <polygon points="700,400 700,225 420,400" fill="var(--corner)"/>
    <line x1="420" y1="400" x2="700" y2="225" stroke="var(--red)" stroke-width="6"/>
  </svg>
  <div class="details__brand">
    <p class="tagline">For all your<br>transport needs</p>
    <div class="wordmark">
      <span class="wordmark__square"></span>
      <span class="wordmark__name">BQL</span>
    </div>
    <p class="company">Groundworks &amp;<br>Freight</p>
  </div>
  <div class="divider-v"></div>
  <div class="contact">
    <p class="contact__name">DOUG PELHAM</p>
    <p class="contact__role">MANAGING DIRECTOR</p>
    <p class="contact__phone">0438 256 904</p>
    <p class="contact__abn">ABN 52<br>907 334 816</p>
  </div>
</section>

<section class="card card--brand" aria-label="Business card, brand side">
  <svg class="card__corners" viewBox="0 0 700 400" aria-hidden="true">
    <polygon points="0,0 240,0 0,85" fill="var(--corner)"/>
    <line x1="0" y1="85" x2="240" y2="0" stroke="var(--red)" stroke-width="6"/>
    <polygon points="700,400 700,255 450,400" fill="var(--corner)"/>
    <line x1="450" y1="400" x2="700" y2="255" stroke="var(--red)" stroke-width="6"/>
  </svg>
  <div class="brand">
    <div class="wordmark">
      <span class="wordmark__square"></span>
      <span class="wordmark__name">BQL</span>
    </div>
    <p class="company">Groundworks &amp;<br>Freight</p>
  </div>
  <p class="services">Earthworks | Haulage | Truck and Machinery Hire<br>Sand, Soil &amp; Mulch Supply | Screening of Products</p>
  <div class="divider-h"></div>
  <div class="brand__contact">
    <p class="brand__phone">0438 256 904</p>
    <p class="brand__email">bqlfreight2010@mailvane.net</p>
  </div>
</section>

</body>
</html>
```